Insurance Agency Flyer

Create a flyer that encompasses the basic services that our agency offers. Flyer wording, logo, and company font are attached. See our website at www.tavumerix.com for additional details.

Target Market(s)

Prospective clients

Industry/Entity Type

Insurance Agency

Other font styles liked:
• baker signet com

```html
<!DOCTYPE html>
<html lang="en">
<head>
<meta charset="utf-8">
<title>The Tavumer Company – Insurance Agency Flyer</title>
<link href="https://fonts.googleapis.com/css2?family=Alegreya+Sans:wght@400;500&family=Marcellus&display=swap" rel="stylesheet">
<style>
  :root {
    --red: #e3193a;
    --ink: #231f20;
    --paper: #ffffff;
    --mist: #ebebeb;
    --text: #2b2b2b;
    --heading: "Marcellus", serif;
    --body: "Alegreya Sans", sans-serif;
  }
  * { margin: 0; padding: 0; box-sizing: border-box; }
  html, body { width: 858px; height: 1200px; overflow: hidden; background: var(--paper); }
  .flyer { position: relative; width: 858px; height: 1200px; background: var(--paper); font-family: var(--body); color: var(--text); overflow: hidden; }
  .abs { position: absolute; }

  .brand { left: 30px; top: 90px; display: flex; align-items: center; gap: 12px; }
  .brand-dot { width: 26px; height: 26px; border-radius: 50%; background: var(--red); }
  .brand-name { font-family: var(--body); font-weight: 500; font-size: 30px; color: var(--red); line-height: 1.05; }

  .about-band { left: 0; top: 208px; width: 858px; height: 169px; background: var(--ink); }
  .about-title { left: 28px; top: 222px; font-family: var(--heading); font-size: 22px; color: #fff; display: flex; align-items: center; gap: 12px; }
  .about-title em { font-style: normal; color: var(--red); }
  .about-title .rule { width: 88px; height: 2px; background: #fff; }
  .about-text { left: 28px; top: 258px; width: 450px; font-size: 15px; line-height: 20.6px; color: #fff; }

  .photo { left: 460px; top: -110px; }

  .tagline-band { left: 0; top: 377px; width: 858px; height: 67px; background: var(--red); }
  .tagline { left: 34px; top: 385px; font-family: var(--heading); font-size: 22px; line-height: 28px; color: #fff; }

  .intro { left: 33px; top: 461px; width: 446px; font-size: 16px; line-height: 22.6px; text-align: justify; }

  .offer-line { left: 0; top: 622px; width: 40px; height: 4px; background: var(--ink); }
  .offer-pill { left: 27px; top: 600px; width: 449px; height: 48px; background: var(--ink); border-radius: 14px; display: flex; align-items: center; padding-left: 14px; font-family: var(--heading); font-size: 20px; color: #fff; }
  .offer-pill em { font-style: normal; color: var(--red); margin-left: 6px; }

  .cover-title { font-family: var(--heading); font-size: 24px; color: var(--red); display: flex; align-items: center; gap: 14px; }
  .cover-title .rule { height: 2px; background: var(--ink); }
  .cover-list { list-style: none; font-size: 17px; line-height: 24px; color: var(--ink); }
  .cover-list li { display: flex; align-items: flex-start; gap: 8px; }
  .cover-list.biz { font-size: 16px; line-height: 22.3px; }
  .tick { flex: none; margin-top: 6px; }

  .choice-head { left: 495px; top: 444px; width: 363px; height: 81px; background: var(--ink); }
  .choice-title { left: 517px; top: 457px; font-family: var(--heading); font-size: 22px; line-height: 28px; color: #fff; }
  .choice-body { left: 495px; top: 525px; width: 363px; height: 450px; background: var(--red); border-bottom-left-radius: 24px; }
  .choice-text { left: 517px; top: 534px; width: 310px; font-size: 15px; line-height: 20.6px; color: #fff; text-align: justify; }

  .quote-band { left: 0; top: 1001px; width: 858px; height: 120px; background: var(--mist); }
  .quote-text { left: 100px; top: 1012px; width: 658px; font-size: 15px; line-height: 20.6px; text-align: center; color: var(--ink); }
  .quote-by { left: 0; top: 1084px; width: 858px; text-align: center; font-size: 15px; color: var(--red); font-family: var(--heading); }
  .quote-by small { font-family: var(--body); font-size: 12px; color: var(--ink); }
  .qmark { font-family: Georgia, serif; font-weight: 700; font-size: 96px; color: var(--red); line-height: 1; }

  .footer { left: 0; top: 1131px; width: 858px; height: 69px; background: var(--ink); }
  .footer-tab { left: 0; top: 1131px; }
  .footer-label { left: 22px; top: 1148px; font-family: var(--body); font-size: 27px; color: #fff; }
  .contact { top: 1144px; display: flex; align-items: center; gap: 14px; font-family: var(--heading); font-size: 34px; color: #fff; }
</style>
</head>
<body>
<main class="flyer">

  <div class="abs brand">
    <span class="brand-dot"></span>
    <span class="brand-name">The Tavumer<br>Company</span>
  </div>

  <div class="abs about-band"></div>

  <svg class="abs photo" width="420" height="600" viewBox="0 0 420 600">
    <defs>
      <linearGradient id="buildingTones" x1="0" y1="0" x2="0" y2="1">
        <stop offset="0" stop-color="#4a63c8"/>
        <stop offset="0.35" stop-color="#8a5a3c"/>
        <stop offset="0.65" stop-color="#b9743e"/>
        <stop offset="0.85" stop-color="#4f6b2a"/>
        <stop offset="1" stop-color="#2f4a1e"/>
      </linearGradient>
    </defs>
    <circle cx="300" cy="278" r="276" fill="var(--ink)"/>
    <circle cx="302" cy="276" r="272" fill="none" stroke="var(--red)" stroke-width="8"/>
    <circle cx="306" cy="274" r="264" fill="url(#buildingTones)" role="img" aria-label="Evening photograph of a lit brick office building with trees"/>
  </svg>

  <div class="abs about-title">ABOUT <em>OUR AGENCY</em><span class="rule"></span></div>
  <p class="abs about-text">Established in 2008, The Tavumer Company was created on the premise that both business and individual consumers should expect more from their insurance agency and agents. The Tavumer Company is a full-service insurance agency that specializes in tailored insurance protection, risk management, and claims consultation.</p>

  <div class="abs tagline-band"></div>
  <h2 class="abs tagline" style="font-weight:400">A PROFESSIONAL AGENCY WITH<br>EXCEPTIONAL SERVICE</h2>

  <p class="abs intro">The Tavumer Company is a firm of proven professionals who are dedicated to caring and conscientious service. We are committed to a high standard of excellence in all that we do and strive to establish a firm relationship of mutual trust and service with each of our clients.</p>

  <div class="abs offer-line"></div>
  <div class="abs offer-pill">WE OFFER <em>COMPLETE INSURANCE SERVICES</em></div>

  <div class="abs cover-title" style="left:41px;top:660px">Personal Coverages<span class="rule" style="width:196px"></span></div>
  <ul class="abs cover-list" style="left:39px;top:706px">
    <li><svg class="tick" width="14" height="14" viewBox="0 0 14 14"><circle cx="7" cy="7" r="6" fill="none" stroke="var(--red)" stroke-width="1.5"/><path d="M4 7.2l2 2 4-4" fill="none" stroke="var(--red)" stroke-width="1.5"/></svg>Homeowners</li>
    <li><svg class="tick" width="14" height="14" viewBox="0 0 14 14"><circle cx="7" cy="7" r="6" fill="none" stroke="var(--red)" stroke-width="1.5"/><path d="M4 7.2l2 2 4-4" fill="none" stroke="var(--red)" stroke-width="1.5"/></svg>Automobile</li>
    <li><svg class="tick" width="14" height="14" viewBox="0 0 14 14"><circle cx="7" cy="7" r="6" fill="none" stroke="var(--red)" stroke-width="1.5"/><path d="M4 7.2l2 2 4-4" fill="none" stroke="var(--red)" stroke-width="1.5"/></svg>Renters / Condo</li>
    <li><svg class="tick" width="14" height="14" viewBox="0 0 14 14"><circle cx="7" cy="7" r="6" fill="none" stroke="var(--red)" stroke-width="1.5"/><path d="M4 7.2l2 2 4-4" fill="none" stroke="var(--red)" stroke-width="1.5"/></svg>Personal umbrella</li>
  </ul>
  <ul class="abs cover-list" style="left:225px;top:706px">
    <li><svg class="tick" width="14" height="14" viewBox="0 0 14 14"><circle cx="7" cy="7" r="6" fill="none" stroke="var(--red)" stroke-width="1.5"/><path d="M4 7.2l2 2 4-4" fill="none" stroke="var(--red)" stroke-width="1.5"/></svg>Valuable Property</li>
    <li><svg class="tick" width="14" height="14" viewBox="0 0 14 14"><circle cx="7" cy="7" r="6" fill="none" stroke="var(--red)" stroke-width="1.5"/><path d="M4 7.2l2 2 4-4" fill="none" stroke="var(--red)" stroke-width="1.5"/></svg>Life</li>
    <li><svg class="tick" width="14" height="14" viewBox="0 0 14 14"><circle cx="7" cy="7" r="6" fill="none" stroke="var(--red)" stroke-width="1.5"/><path d="M4 7.2l2 2 4-4" fill="none" stroke="var(--red)" stroke-width="1.5"/></svg>Disability</li>
    <li><svg class="tick" width="14" height="14" viewBox="0 0 14 14"><circle cx="7" cy="7" r="6" fill="none" stroke="var(--red)" stroke-width="1.5"/><path d="M4 7.2l2 2 4-4" fill="none" stroke="var(--red)" stroke-width="1.5"/></svg>Health</li>
  </ul>

  <div class="abs cover-title" style="left:39px;top:815px">Business Coverages<span class="rule" style="width:196px"></span></div>
  <ul class="abs cover-list biz" style="left:38px;top:858px">
    <li><svg class="tick" width="14" height="14" viewBox="0 0 14 14"><circle cx="7" cy="7" r="6" fill="none" stroke="var(--red)" stroke-width="1.5"/><path d="M4 7.2l2 2 4-4" fill="none" stroke="var(--red)" stroke-width="1.5"/></svg>Commercial General Liability</li>
    <li><svg class="tick" width="14" height="14" viewBox="0 0 14 14"><circle cx="7" cy="7" r="6" fill="none" stroke="var(--red)" stroke-width="1.5"/><path d="M4 7.2l2 2 4-4" fill="none" stroke="var(--red)" stroke-width="1.5"/></svg>Commercial Property</li>
    <li><svg class="tick" width="14" height="14" viewBox="0 0 14 14"><circle cx="7" cy="7" r="6" fill="none" stroke="var(--red)" stroke-width="1.5"/><path d="M4 7.2l2 2 4-4" fill="none" stroke="var(--red)" stroke-width="1.5"/></svg>Workers’ Compensation</li>
    <li><svg class="tick" width="14" height="14" viewBox="0 0 14 14"><circle cx="7" cy="7" r="6" fill="none" stroke="var(--red)" stroke-width="1.5"/><path d="M4 7.2l2 2 4-4" fill="none" stroke="var(--red)" stroke-width="1.5"/></svg>Business Automobile</li>
    <li><svg class="tick" width="14" height="14" viewBox="0 0 14 14"><circle cx="7" cy="7" r="6" fill="none" stroke="var(--red)" stroke-width="1.5"/><path d="M4 7.2l2 2 4-4" fill="none" stroke="var(--red)" stroke-width="1.5"/></svg>Commercial Excess Liability</li>
  </ul>
  <ul class="abs cover-list biz" style="left:290px;top:858px">
    <li><svg class="tick" width="14" height="14" viewBox="0 0 14 14"><circle cx="7" cy="7" r="6" fill="none" stroke="var(--red)" stroke-width="1.5"/><path d="M4 7.2l2 2 4-4" fill="none" stroke="var(--red)" stroke-width="1.5"/></svg>Professional Liability</li>
    <li><svg class="tick" width="14" height="14" viewBox="0 0 14 14"><circle cx="7" cy="7" r="6" fill="none" stroke="var(--red)" stroke-width="1.5"/><path d="M4 7.2l2 2 4-4" fill="none" stroke="var(--red)" stroke-width="1.5"/></svg>Employment Practices<br>Liability</li>
    <li><svg class="tick" width="14" height="14" viewBox="0 0 14 14"><circle cx="7" cy="7" r="6" fill="none" stroke="var(--red)" stroke-width="1.5"/><path d="M4 7.2l2 2 4-4" fill="none" stroke="var(--red)" stroke-width="1.5"/></svg>Life</li>
    <li><svg class="tick" width="14" height="14" viewBox="0 0 14 14"><circle cx="7" cy="7" r="6" fill="none" stroke="var(--red)" stroke-width="1.5"/><path d="M4 7.2l2 2 4-4" fill="none" stroke="var(--red)" stroke-width="1.5"/></svg>Health</li>
  </ul>

  <div class="abs choice-head"></div>
  <h2 class="abs choice-title" style="font-weight:400">WE ARE AN INDEPENDENT<br>CLEARPATH CHOICE AGENCY</h2>
  <div class="abs choice-body"></div>
  <p class="abs choice-text">Being an Independent Clearpath Choice Agency means that we take our time to make sure that we learn about your needs, and that each policy is built to specifically meet those needs. We are committed to treating you as a person not another policy number. We will work with you to identify the insurance products and services that are right for you, your family, and/or your business. We accomplish this by using our expertise and multiple insurance carrier relationships to customize your insurance program. We will explain the different coverage and options available to you, and should the need arise, we will be there to guide you through the claims process. Our promise to you is that we will return your phone calls and emails promptly and respond to you requests in a timely manner. Also, we work diligently to stay informed about the latest insurance trends to understand how they might affect our clients.</p>

  <div class="abs quote-band"></div>
  <div class="abs qmark" style="left:50px;top:982px">“</div>
  <div class="abs qmark" style="left:740px;top:1062px">”</div>
  <p class="abs quote-text">The Tavumer Company has consistently responded to the needs of our business, finding us well priced policies without sacrificing coverage. They always respond to our needs quickly and effectively, provide great consultation, are knowledgeable, and care greatly about our business and success.</p>
  <p class="abs quote-by">DANA HOLLIS <small>(Long time client)</small></p>

  <div class="abs footer"></div>
  <svg class="abs footer-tab" width="200" height="69" viewBox="0 0 200 69"><polygon points="0,0 175,0 199,69 0,69" fill="var(--red)"/><polygon points="175,0 180,0 204,69 199,69" fill="#fff"/></svg>
  <div class="abs footer-label">Get in Touch</div>
  <div class="abs contact" style="left:210px">
    <svg width="32" height="32" viewBox="0 0 32 32"><circle cx="16" cy="16" r="15" fill="var(--red)"/><path d="M11 9c1-1 2.5-.5 3 .7l1 2.3c.3.8 0 1.5-.6 2l-1 .8c.8 1.8 2.2 3.2 4 4l.8-1c.5-.6 1.2-.9 2-.6l2.3 1c1.2.5 1.7 2 .7 3-1.2 1.2-3 1.8-4.8 1-4.3-1.8-7.5-5-9.3-9.3-.8-1.8-.2-3.6.9-4.9z" fill="#fff"/></svg>
    <span>555.0142.800</span>
  </div>
  <div class="abs contact" style="left:490px">
    <svg width="32" height="32" viewBox="0 0 32 32"><circle cx="16" cy="16" r="15" fill="var(--red)"/><g fill="none" stroke="var(--ink)" stroke-width="1.6"><circle cx="16" cy="16" r="8"/><ellipse cx="16" cy="16" rx="3.5" ry="8"/><path d="M8 16h16M9.5 12h13M9.5 20h13"/></g></svg>
    <span>www.tavumerix.com</span>
  </div>

</main>
</body>
</html>
```